Global Expert Network Firm needs business card design

We need business card design for a new company based in Seoul, South Korea called 'Corwell Insight Partners'. We recruit industry experts covering all countries and connect our client and recruited expert by phone, face-to-face meetings and etc. We are a global expert network firm that is focused on delivering high-quality experts to our clients throughout the world. Our clients include multinational corporations, global consulting firms, private equity firms, venture capital firms, asset management companies.
We have made new logo and please find attachment.(Please use new logo)
Target Market(s)
Global Consulting Firms, Investment Firms, Private Equity Firms, Venture Capital Firms.
Industry/Entity Type
Recruitment
Contact Information for Business Card
We need two Languages (English and Korean Version).
The front is Korean and the back is English version.
[The back] [English]
Company Name: Corwell Insight Partners, Inc.
CEO Name: Daniel Park
Address: #507, Hanbit Bldg, 82 Maebongsan-ro, Dobong-gu, Seoul, 01327, Korea
Tel. +82 2 718 4052
Fax. +82 2 864 1097
Mobile. +82 10 7264 8815
Email: daniel@corwellip.com
Web: www.corwellip.com
[The front] [Korean] => Described in same order as English version.
회사명: 코웰인사이트파트너스(주)
대표이사: 박도현
주소: 서울시 도봉구 매봉산로 82 한빛빌딩 507호
Tel. 02 718 4052
Fax. 02 864 1097
Mobile. 010 7264 8815
Web: www.corwellip.com
Look and feel
Each slider illustrates characteristics of the customer's brand and the style your logo design should communicate.

```html
<!DOCTYPE html>
<html lang="en">
<head>
<meta charset="utf-8">
<title>Corwell Insight Partners – Business Cards</title>
<link href="https://fonts.googleapis.com/css2?family=Arimo:wght@400;700&family=Nanum+Myeongjo:wght@400;700&display=swap" rel="stylesheet">
<style>
  :root {
    --navy: #1f2359;
    --grey-text: #6f6f73;
    --grey-band: #8a8a8c;
    --rule: #b9b9bb;
    --paper: #f7f7f5;
    --backdrop: #2b2c2f;
  }
  * { margin: 0; padding: 0; box-sizing: border-box; }
  html, body { width: 1200px; height: 1200px; overflow: hidden; }
  body {
    background: var(--backdrop);
    font-family: "Arimo", Arial, sans-serif;
    position: relative;
  }
  .card {
    position: absolute;
    left: 285px;
    width: 630px;
    height: 360px;
    background: var(--paper);
    overflow: hidden;
  }
  .card--english { top: 158px; }
  .card--korean { top: 682px; }

  .brand {
    position: absolute;
    left: 84px;
    top: 150px;
    width: 160px;
    display: flex;
    align-items: flex-start;
    gap: 10px;
  }
  .brand__square {
    flex: none;
    width: 14px;
    height: 14px;
    margin-top: 4px;
    background: var(--navy);
  }
  .brand__name {
    font-family: "Arimo", Arial, sans-serif;
    font-weight: 400;
    font-size: 19px;
    line-height: 1.25;
    letter-spacing: 0.04em;
    text-transform: uppercase;
    color: var(--navy);
  }

  .divider-accent {
    position: absolute;
    left: 302px; top: 58px;
    width: 3px; height: 50px;
    background: var(--navy);
  }
  .divider-rule {
    position: absolute;
    left: 303px; top: 133px;
    width: 1.5px; height: 155px;
    background: var(--rule);
  }

  .person {
    position: absolute;
    left: 354px; top: 68px;
  }
  .person__name {
    font-size: 20px;
    font-weight: 700;
    color: var(--navy);
    line-height: 1;
  }
  .person__title {
    font-size: 14px;
    color: var(--grey-text);
    margin-top: 3px;
  }
  .card--korean .person { top: 62px; }
  .card--korean .person__name {
    font-family: "Nanum Myeongjo", serif;
    font-size: 25px;
    font-weight: 700;
  }
  .card--korean .person__title {
    font-family: "Nanum Myeongjo", serif;
    font-size: 13px;
    margin-top: 0;
  }

  .address {
    position: absolute;
    left: 354px; top: 137px;
    font-size: 14.5px;
    line-height: 18px;
    color: var(--grey-text);
    font-style: normal;
  }
  .card--korean .address {
    font-family: "Nanum Myeongjo", serif;
    font-size: 15px;
    top: 140px;
  }

  .contacts {
    position: absolute;
    left: 354px; top: 218px;
    list-style: none;
    font-size: 14.5px;
    line-height: 18px;
    color: var(--grey-text);
  }
  .card--korean .contacts { top: 214px; }
  .contacts li { display: flex; align-items: center; gap: 8px; }
  .contacts svg { width: 11px; height: 11px; flex: none; }

  .footer-band {
    position: absolute;
    left: 0; bottom: 0;
    width: 630px; height: 36px;
  }
  .website {
    position: absolute;
    left: 0; right: 0; bottom: 13px;
    text-align: center;
    color: #fff;
    font-size: 13.5px;
    letter-spacing: 0.12em;
  }
  .website b { font-weight: 700; }
</style>
</head>
<body>

<section class="card card--english" aria-label="English side">
  <div class="brand">
    <span class="brand__square"></span>
    <span class="brand__name">Corwell<br>Insight<br>Partners</span>
  </div>
  <span class="divider-accent"></span>
  <span class="divider-rule"></span>
  <div class="person">
    <p class="person__name">Daniel Park</p>
    <p class="person__title">CEO</p>
  </div>
  <address class="address">
    Corwell Insight Partners, Inc.<br>
    #507, Hanbit Bldg<br>
    82 Maebongsan-ro, Dobong-gu<br>
    Seoul, 01327, Korea
  </address>
  <ul class="contacts">
    <li><svg viewBox="0 0 12 12"><path d="M2 1 L4.5 1 L5.2 3.6 L3.8 4.6 C4.5 6.2 5.8 7.5 7.4 8.2 L8.4 6.8 L11 7.5 L11 10 C11 10.6 10.5 11 10 11 C5.3 11 1 6.7 1 2 C1 1.5 1.4 1 2 1 Z" fill="var(--navy)"/></svg>+82 2 718 4052</li>
    <li><svg viewBox="0 0 12 12"><rect x="3" y="1" width="6" height="3" fill="var(--navy)"/><rect x="1" y="4.5" width="10" height="5" rx="1" fill="var(--navy)"/><rect x="3" y="8" width="6" height="3" fill="var(--navy)"/></svg>+82 2 864 1097</li>
    <li><svg viewBox="0 0 12 12"><rect x="3" y="0.5" width="6.5" height="11" rx="1" fill="none" stroke="var(--navy)" stroke-width="1.3"/><circle cx="6.25" cy="9.5" r="0.7" fill="var(--navy)"/></svg>+82 10 7264 8815</li>
    <li><svg viewBox="0 0 12 12"><rect x="0.8" y="2.5" width="10.4" height="7" fill="none" stroke="var(--navy)" stroke-width="1.1"/><path d="M1 3 L6 7 L11 3" fill="none" stroke="var(--navy)" stroke-width="1.1"/></svg>daniel@corwellip.com</li>
  </ul>
  <svg class="footer-band" viewBox="0 0 630 36" aria-hidden="true">
    <rect x="0" y="13" width="630" height="10" fill="var(--grey-band)"/>
    <rect x="0" y="24" width="630" height="12" fill="var(--navy)"/>
    <path d="M145 26 C170 26 178 0 205 0 L425 0 C452 0 460 26 485 26 Z" fill="var(--navy)"/>
    <path d="M0 24 L145 24 C170 24 178 1 205 1" fill="none" stroke="#fff" stroke-width="1.5"/>
    <path d="M630 24 L485 24 C460 24 452 1 425 1" fill="none" stroke="#fff" stroke-width="1.5"/>
  </svg>
  <p class="website">www.<b>corwellip</b>.com</p>
</section>

<section class="card card--korean" aria-label="Korean side" lang="ko">
  <div class="brand">
    <span class="brand__square"></span>
    <span class="brand__name" lang="en">Corwell<br>Insight<br>Partners</span>
  </div>
  <span class="divider-accent"></span>
  <span class="divider-rule"></span>
  <div class="person">
    <p class="person__name">박도현</p>
    <p class="person__title">대표이사</p>
  </div>
  <address class="address">
    코웰인사이트파트너스(주)<br>
    서울시 도봉구 매봉산로<br>
    82 한빛빌딩 507호
  </address>
  <ul class="contacts">
    <li><svg viewBox="0 0 12 12"><path d="M2 1 L4.5 1 L5.2 3.6 L3.8 4.6 C4.5 6.2 5.8 7.5 7.4 8.2 L8.4 6.8 L11 7.5 L11 10 C11 10.6 10.5 11 10 11 C5.3 11 1 6.7 1 2 C1 1.5 1.4 1 2 1 Z" fill="var(--navy)"/></svg>+82 2 718 4052</li>
    <li><svg viewBox="0 0 12 12"><rect x="3" y="1" width="6" height="3" fill="var(--navy)"/><rect x="1" y="4.5" width="10" height="5" rx="1" fill="var(--navy)"/><rect x="3" y="8" width="6" height="3" fill="var(--navy)"/></svg>+82 2 864 1097</li>
    <li><svg viewBox="0 0 12 12"><rect x="3" y="0.5" width="6.5" height="11" rx="1" fill="none" stroke="var(--navy)" stroke-width="1.3"/><circle cx="6.25" cy="9.5" r="0.7" fill="var(--navy)"/></svg>+82 10 7264 8815</li>
    <li><svg viewBox="0 0 12 12"><rect x="0.8" y="2.5" width="10.4" height="7" fill="none" stroke="var(--navy)" stroke-width="1.1"/><path d="M1 3 L6 7 L11 3" fill="none" stroke="var(--navy)" stroke-width="1.1"/></svg>daniel@corwellip.com</li>
  </ul>
  <svg class="footer-band" viewBox="0 0 630 36" aria-hidden="true">
    <rect x="0" y="13" width="630" height="10" fill="var(--grey-band)"/>
    <rect x="0" y="24" width="630" height="12" fill="var(--navy)"/>
    <path d="M145 26 C170 26 178 0 205 0 L425 0 C452 0 460 26 485 26 Z" fill="var(--navy)"/>
    <path d="M0 24 L145 24 C170 24 178 1 205 1" fill="none" stroke="#fff" stroke-width="1.5"/>
    <path d="M630 24 L485 24 C460 24 452 1 425 1" fill="none" stroke="#fff" stroke-width="1.5"/>
  </svg>
  <p class="website" lang="en">www.<b>corwellip</b>.com</p>
</section>

</body>
</html>
```